Web Design Project (Renewable Energy Services Company)

Hello crowd,

We are looking to create a website for a new company. We would like to have the page already coded, if you do not provide the code as well, please indicate so. I am including a very preliminary approximation of the wireframe.

We do not have the logo either the color pallet, however we have in mind couple websites that would be similar tho these.

http://www.brivolen.com/en/

and

http://www.tarmuvex.com/

We did an approximated wireframe our our website, not necesarly to decide on the layout but rather to know how many pages will be needed. It would be around 10 pages. We will need a section that will be an e-commerce page to sell products such as engineering instrumentation, software and consumables such as cable and connectors.

Our company will be called ORVIK. We will be based in Monterrey, Mexico. Our focused will be the development of renewable energy projects. Similar scope of services than http://www.brivolen.com/en/ but only for wind and solar projects.

We like something minimalistic. Some of the things that the logo might or might not include would be the monterrey famous hill, but not strictly necessary.
http://en.plavorinet.org/wiki/Loma_del_Trueno

also ORVIK (which stands for ORganica VIKtoria) the name is similar the bird (seagal) or wind turbines and sun...any of these are only suggestions and we are open to receive any proposals.

There must be a
home page
services page (some subsections)
products page (some subsections)
contact page with contact form

and some additional subsections like careers and partnerships.

We are very excited to start hearing about this project.
Updates

Please for the logo, do not restrict your ideas to the ones provided as it has generated too specific logos. Pleae just allow your imagination to flow for a company that develops renewable energy projects.

Target Market(s)

large companies interested in developing renewable energy projects

Industry/Entity Type

E-Commerce

Requirements
Must have
• Minimalistic and unique design.
Nice to have
• contact form to save contacts in a database

Should not have
• We are looking a very minimalistic logo. It should not be an explicit wind turbine a seagal or anything like that. we are looking for abstract, simple and minimalistic image.

```html
<!DOCTYPE html>
<html lang="en">
<head>
<meta charset="utf-8">
<title>ORVIK – Renewable Energy Projects</title>
<link href="https://fonts.googleapis.com/css2?family=Ubuntu+Condensed&family=Open+Sans:wght@700&display=swap" rel="stylesheet">
<style>
  :root {
    --sky-top: #2f6db8;
    --sky-mid: #6f9fd2;
    --sky-low: #b9d2ea;
    --panel-blue: #1f5aa8;
    --panel-deep: #15396f;
    --header-fill: rgba(44, 104, 182, 0.72);
    --frame-line: rgba(255, 255, 255, 0.85);
    --nav-button: rgba(150, 190, 236, 0.62);
    --tab-button: #4a8fc6;
    --search-fill: rgba(150, 190, 236, 0.55);
    --text-light: #ffffff;
    --text-soft: #dbe8f6;
    --card-teal-dark: #14566a;
    --card-teal: #1d8a8c;
    --card-navy: #145b8c;
    --footer-fill: rgba(46, 54, 62, 0.78);
    --footer-text: #b8c2cc;
    --icon-a: #5fb4df;
    --icon-b: #3a6fc4;
    --icon-c: #d8dde2;
    --icon-d: #f08b2c;
  }
  * { box-sizing: border-box; margin: 0; padding: 0; }
  html, body { width: 1200px; height: 1003px; overflow: hidden; }
  body { font-family: "Open Sans", Arial, sans-serif; color: var(--text-light); }

  .page { position: relative; width: 1200px; height: 1003px; overflow: hidden; }

  .hero-photo {
    position: absolute; inset: 0;
    background:
      linear-gradient(160deg, transparent 30%, rgba(20, 50, 120, 0.75) 55%, rgba(25, 60, 140, 0.6) 80%, transparent 95%),
      linear-gradient(180deg, var(--sky-top) 0%, var(--sky-mid) 45%, var(--sky-low) 100%);
  }

  /* Header */
  .site-header {
    position: absolute; left: 19px; top: 26px; width: 1161px; height: 185px;
    background: var(--header-fill);
    border: 2px solid var(--frame-line); border-radius: 10px;
  }
  .brand { position: absolute; left: 60px; top: 55px; display: flex; align-items: center; gap: 20px; }
  .brand-mark { width: 84px; height: 84px; border-radius: 50%; background: var(--panel-deep); }
  .brand-name { font-family: "Ubuntu Condensed", sans-serif; font-size: 62px; letter-spacing: 3px; color: var(--text-light); line-height: 1; }

  .account-links {
    position: absolute; top: 20px; right: 66px;
    display: flex; gap: 22px; font-size: 13px; letter-spacing: 1px; color: var(--text-soft);
  }
  .account-links .greeting { margin-right: 18px; }

  .main-nav { position: absolute; top: 68px; left: 519px; display: flex; gap: 14px; }
  .main-nav a, .sub-nav a {
    display: block; text-decoration: none; color: var(--text-light);
    font-family: "Ubuntu Condensed", sans-serif; text-align: center;
  }
  .main-nav a {
    width: 134px; height: 40px; line-height: 40px; font-size: 20px; letter-spacing: 1.5px;
    background: var(--nav-button); border-radius: 7px;
  }

  .search {
    position: absolute; left: 775px; top: 127px; width: 325px; height: 44px;
    background: var(--search-fill); border-radius: 8px;
    font-family: "Ubuntu Condensed", sans-serif; font-size: 19px; letter-spacing: 1.5px;
    color: rgba(255,255,255,0.6); line-height: 44px; padding-left: 18px;
  }
  .search svg { position: absolute; right: 8px; top: 10px; }

  .sub-nav { position: absolute; left: 61px; top: 211px; display: flex; gap: 19px; }
  .sub-nav a {
    width: 120px; height: 36px; line-height: 34px; font-size: 21px;
    background: var(--tab-button); border-radius: 0 0 7px 7px;
  }

  /* Product cards */
  .product-card {
    position: absolute; width: 343px; height: 186px; border-radius: 9px;
  }
  .product-card.instrumentation { left: 831px; top: 253px; background: var(--card-teal-dark); }
  .product-card.software { left: 832px; top: 449px; background: var(--card-teal); }
  .product-card.cabling { left: 834px; top: 643px; background: var(--card-navy); }
  .card-title {
    position: absolute; left: 12px; top: 7px; right: 12px; height: 36px;
    border: 1px solid rgba(255,255,255,0.45); border-radius: 9px;
    background: rgba(255,255,255,0.06);
    font-family: "Ubuntu Condensed", sans-serif; font-size: 21px; line-height: 34px; padding-left: 14px;
  }
  .card-image { position: absolute; left: 13px; top: 60px; width: 131px; height: 105px; }
  .instrumentation .card-image { background: linear-gradient(180deg, #3f7bc2, #9fc3e3 70%, #c9b34a); }
  .software .card-image { background: linear-gradient(180deg, #f4f4f4, #c9cfd6); }
  .cabling .card-image { background: linear-gradient(135deg, #8fc6e6, #2d7fb6); }
  .card-text {
    position: absolute; left: 156px; top: 58px; width: 180px;
    font-size: 12.5px; line-height: 21px; letter-spacing: 0.4px;
  }
  .read-more {
    position: absolute; right: 9px; bottom: 6px; font-size: 12.5px; letter-spacing: 0.5px; color: var(--text-light); text-decoration: none;
  }

  /* Footer */
  .site-footer {
    position: absolute; left: 25px; top: 866px; width: 1161px; height: 116px;
    background: var(--footer-fill); border: 2px solid var(--frame-line); border-radius: 10px;
  }
  .footer-nav { position: absolute; left: 152px; top: 34px; display: flex; gap: 44px; font-size: 14px; letter-spacing: 0.8px; }
  .footer-nav a, .footer-legal a { color: var(--footer-text); text-decoration: none; }
  .footer-legal { position: absolute; left: 66px; top: 64px; display: flex; gap: 39px; font-size: 13px; letter-spacing: 0.6px; color: var(--footer-text); }
  .social { position: absolute; left: 976px; top: 44px; display: flex; gap: 11px; }
  .social span { width: 27px; height: 27px; border-radius: 4px; display: block; }
  .social .s1 { background: var(--icon-a); }
  .social .s2 { background: var(--icon-b); }
  .social .s3 { background: var(--icon-c); }
  .social .s4 { background: var(--icon-d); }
</style>
</head>
<body>
<div class="page">
  <div class="hero-photo" role="img" aria-label="Rows of tilted solar panels under a blue sky with white clouds"></div>

  <header class="site-header">
    <div class="brand">
      <span class="brand-mark"></span>
      <span class="brand-name">ORVIK</span>
    </div>
    <div class="account-links">
      <span class="greeting">Welcome, Guest</span>
      <span>LOGIN</span>
      <span>REGISTER</span>
    </div>
    <nav class="main-nav">
      <a href="#">Home</a>
      <a href="#">Services</a>
      <a href="#">Products</a>
      <a href="#">Contact Us</a>
    </nav>
    <div class="search">Serach
      <svg width="24" height="24" viewBox="0 0 24 24" aria-hidden="true">
        <circle cx="12" cy="12" r="10" fill="none" stroke="rgba(255,255,255,0.75)" stroke-width="2"/>
        <circle cx="12" cy="12" r="6" fill="none" stroke="rgba(255,255,255,0.75)" stroke-width="2"/>
        <circle cx="12" cy="12" r="2.5" fill="rgba(255,255,255,0.75)"/>
      </svg>
    </div>
  </header>

  <nav class="sub-nav">
    <a href="#">News</a>
    <a href="#">About Us</a>
  </nav>

  <section class="product-card instrumentation">
    <h2 class="card-title">Engineering Instrumentation</h2>
    <div class="card-image" role="img" aria-label="Wind turbines on a field under a cloudy sky"></div>
    <p class="card-text">Lorem ipsum dolor sit amet, consec tetuer adipiscing elit. Praesent vestibulum molestie lacus.</p>
    <a class="read-more" href="#">Read More</a>
  </section>

  <section class="product-card software">
    <h2 class="card-title">Software and Consumables</h2>
    <div class="card-image" role="img" aria-label="Puzzle pieces joined with small computers on top"></div>
    <p class="card-text">Lorem ipsum dolor sit amet, consec tetuer adipiscing elit. Praesent vestibulum molestie lacus.</p>
    <a class="read-more" href="#">Read More</a>
  </section>

  <section class="product-card cabling">
    <h2 class="card-title">Cable and Connectors</h2>
    <div class="card-image" role="img" aria-label="Close view of network cables and connectors"></div>
    <p class="card-text">Lorem ipsum dolor sit amet, consec tetuer adipiscing elit. Praesent vestibulum molestie lacus.</p>
    <a class="read-more" href="#">Read More</a>
  </section>

  <footer class="site-footer">
    <nav class="footer-nav">
      <a href="#">Home</a>
      <a href="#">Services</a>
      <a href="#">Products</a>
      <a href="#">Contact Us</a>
    </nav>
    <div class="footer-legal">
      <span>Copyright © 2012 BRIVOLEN, Inc. All Rights Reserved</span>
      <a href="#">Terms of Use</a>
      <a href="#">Privacy Policy</a>
    </div>
    <div class="social" aria-label="Social links">
      <span class="s1"></span>
      <span class="s2"></span>
      <span class="s3"></span>
      <span class="s4"></span>
    </div>
  </footer>
</div>
</body>
</html>
```